Commercial construction contractor website.

We need a website that contains About Us, Contact info, Services, Project pictures and Industry News section

Target Market(s)

I'm building industral/flex spaces/commercial.

Industry/Entity Type

Commercial/industrial construction

Coding

Coded - Design and coding required

Number of Pages Required

5+ page

Font styles to use
Other font styles liked:
• The logo font is Microgramma Pro

Requirements
Must have
• Must have correct company name spelling: Halden Ridge Construction
Nice to have
• I do like to see our logo design implemented in the design
Should not have
• Please do not show big city pictures and business suit people. We are a commercial construction company

```html
<!DOCTYPE html>
<html lang="en">
<head>
<meta charset="utf-8">
<title>Halden Ridge Construction</title>
<link rel="stylesheet" href="https://fonts.googleapis.com/css2?family=Michroma&family=Montserrat:wght@400;500;600;700&display=swap">
<style>
:root{
  --blue:#0b6cbd;
  --blue-deep:#0a5ea8;
  --title:#1a73bb;
  --dark:#2a2e33;
  --text:#333;
  --muted:#666;
  --light:#f3f4f6;
  --white:#fff;
}
*{box-sizing:border-box;margin:0;padding:0}
html,body{width:1200px;height:5008px;overflow:hidden}
body{position:relative;font-family:"Montserrat",sans-serif;color:var(--text);background:var(--white)}
.abs{position:absolute}
.topbar{left:0;top:0;width:1200px;height:27px;background:var(--blue);color:var(--white)}
.topbar .call{position:absolute;right:92px;top:4px;font-size:15px}
.topbar .call b{font-weight:700;margin-left:14px;font-size:17px}
.topbar .social{position:absolute;right:18px;top:7px;display:flex;gap:6px}
.topbar .social span{width:13px;height:13px;border-radius:50%;background:var(--white)}
.header{left:0;top:27px;width:1200px;height:78px;background:var(--white)}
.brand{position:absolute;left:24px;top:22px;display:flex;align-items:center;gap:10px}
.brand i{width:26px;height:26px;background:var(--blue)}
.brand span{font-family:"Michroma",sans-serif;font-size:12px;color:var(--blue-deep);line-height:1.25;width:130px}
.nav{position:absolute;right:18px;top:40px;display:flex;gap:56px;font-size:13px;color:#222}
.nav .active{border-bottom:3px solid var(--blue);padding-bottom:6px}
.hero{left:0;top:105px;width:1200px;height:389px;background:linear-gradient(180deg,#5d5f63 0%,#a6a8ab 45%,#d9dadc 75%,#8d8f92 100%)}
.hero h1{position:absolute;left:0;width:1200px;top:90px;text-align:center;font-family:"Michroma",sans-serif;font-weight:400;font-size:33px;color:var(--white);letter-spacing:5px;line-height:62px}
.btn-ghost{position:absolute;left:473px;top:220px;width:254px;height:48px;border:2px solid var(--white);color:var(--white);font-size:15px;display:flex;align-items:center;justify-content:center}
.dots{position:absolute;left:0;width:1200px;top:349px;display:flex;justify-content:center;gap:14px}
.dots span{width:22px;height:22px;border-radius:50%;background:var(--white)}
.dots span:first-child{background:var(--blue)}
.about{left:0;top:494px;width:1200px;height:571px;background:#fafbfc}
.about .kicker{position:absolute;left:20px;top:74px;font-size:24px;color:#222}
.about h2{position:absolute;left:20px;top:112px;font-size:33px;font-weight:600;color:var(--title)}
.about p{position:absolute;left:20px;top:172px;width:570px;font-size:21px;line-height:34px;color:#333}
.btn{position:absolute;background:var(--blue);color:var(--white);font-size:20px;display:flex;align-items:center;justify-content:center}
.about .btn{left:20px;top:384px;width:220px;height:44px}
.photo{position:absolute}
.section-title{position:absolute;left:0;width:1200px;text-align:center;font-size:33px;font-weight:600;color:var(--title)}
.section-title span{border-bottom:5px solid var(--blue-deep);padding-bottom:2px}
.tile{position:absolute;top:1241px;width:227px;height:341px}
.tile .label{position:absolute;left:0;bottom:0;width:100%;height:45px;background:rgba(40,40,40,.75);color:var(--white);font-weight:700;font-size:24px;text-align:center;line-height:45px;letter-spacing:1px}
.btn-raised{position:absolute;left:473px;width:254px;height:54px;background:var(--blue);color:var(--white);font-size:21px;display:flex;align-items:center;justify-content:center;border-radius:4px;box-shadow:0 4px 0 #0a3f70}
.stats{left:0;top:1743px;width:1200px;height:348px;display:flex}
.stat{flex:1;display:flex;flex-direction:column;align-items:center;justify-content:center;color:var(--white)}
.stat.blue{background:linear-gradient(180deg,#1f6fb8,#0b5fae)}
.stat.dark{background:linear-gradient(180deg,#2d3238,#4a4e53)}
.stat strong{font-size:52px;font-weight:600;line-height:60px}
.stat small{font-size:17px;text-align:center;line-height:22px;margin-top:6px}
.stars{display:flex;gap:8px}
.clients{left:0;top:2995px;width:1200px;height:385px;background:#eef0f3}
.client{position:absolute;top:205px;width:102px;height:96px;background:var(--white);display:flex;flex-direction:column;align-items:center;justify-content:center;gap:6px}
.client i{width:20px;height:20px;background:var(--blue-deep)}
.client span{font-size:12px;font-weight:600;color:var(--blue-deep)}
.avatar{left:525px;top:3585px;width:150px;height:150px;border-radius:50%;border:6px solid var(--blue-deep);background:radial-gradient(circle,#cfd6dc,#7e8c98)}
.arrow{position:absolute;top:3725px;width:54px;height:54px}
.quote{left:230px;top:3770px;width:740px;text-align:center;font-size:21px;font-weight:600;line-height:31px;color:#222}
.who{left:494px;top:3876px}
.who b{display:block;font-size:23px;color:var(--title);font-weight:600}
.who small{font-size:13px;color:#555}
.news{left:0;top:3997px;width:1200px;height:688px;background:#f4f5f7}
.card{position:absolute;top:4172px;width:343px}
.card .img{height:150px}
.card p{margin-top:36px;font-size:17px;line-height:23px;text-align:center;color:#333}
.card .more{display:flex;margin:18px auto 0;width:214px;height:37px;border:2px solid var(--blue);align-items:center;justify-content:center;font-size:17px;font-weight:600;color:#222;background:var(--white)}
.footer{left:0;top:4685px;width:1200px;height:323px;background:var(--blue);color:var(--white)}
.foot-nav{position:absolute;left:18px;top:22px;font-size:14px;line-height:30px}
.foot-form{position:absolute;left:326px;top:22px;width:410px;font-size:14px;line-height:29px}
.field{position:absolute;background:#e0e0e0;color:#555;font-size:14px;padding-left:14px;line-height:30px;height:30px}
.send{position:absolute;left:328px;top:238px;width:158px;height:28px;border:2px solid var(--white);font-size:14px;text-align:center;line-height:24px}
.follow{position:absolute;left:935px;top:22px;font-size:14px}
.follow-icons{position:absolute;left:940px;top:70px;display:flex;gap:26px}
.follow-icons span{width:48px;height:48px;border-radius:50%;background:rgba(255,255,255,.9)}
.legal{position:absolute;right:18px;top:268px;text-align:right;font-size:12px;line-height:18px}
</style>
</head>
<body>

<div class="abs topbar">
  <div class="call">Call us <b>555 0142 0199</b></div>
  <div class="social" aria-label="social links"><span></span><span></span><span></span></div>
</div>

<header class="abs header">
  <div class="brand"><i></i><span>HALDEN RIDGE CONSTRUCTION</span></div>
  <nav class="nav">
    <span class="active">HOME</span><span>ABOUT US</span><span>SERVICES</span><span>PROJECTS</span><span>NEWS</span><span>CONTACT</span>
  </nav>
</header>

<section class="abs hero" role="img" aria-label="Empty industrial warehouse interior with steel roof and overhead lights">
  <h1>WELCOME TO<br>HALDEN RIDGE CONSTRUCTION</h1>
  <div class="btn-ghost">REQUEST INFORMATION</div>
  <div class="dots"><span></span><span></span><span></span><span></span></div>
</section>

<section class="abs about">
  <div class="kicker">ABOUT</div>
  <h2>HALDEN RIDGE CONSTRUCTION</h2>
  <p>Lorem ipsum dolor sit amet, consectetur adipiscing elit, sed do eiusmod tempor incididunt ut labore et dolore magna aliqua. Quis ipsum suspendisse ultrices gravida. Risus commodo viverra maecena accumsan lacus vel facilisis.</p>
  <div class="btn">READ MORE</div>
  <div class="photo" style="left:640px;top:78px;width:543px;height:413px;background:linear-gradient(160deg,#3b3b3b,#8a7f76 55%,#b7b2ad)" role="img" aria-label="Converted industrial office with brick walls, arched windows and desks"></div>
</section>

<h2 class="section-title" style="top:1130px"><span>WHAT</span> WE DO</h2>
<div class="tile" style="left:17px;background:linear-gradient(180deg,#8fc1ec,#2f6fc0 55%,#8c8f93)" role="img" aria-label="Blue clad industrial building"><div class="label">SERVICE 1</div></div>
<div class="tile" style="left:252px;background:linear-gradient(180deg,#6fa9e0,#cfd2d5 45%,#8f9398)" role="img" aria-label="Grey warehouse with red framed entrance"><div class="label">SERVICE 2</div></div>
<div class="tile" style="left:487px;background:linear-gradient(180deg,#1f5ea8,#2b2b2f 40%,#5e7d48)" role="img" aria-label="Dark commercial facade with red trim"><div class="label">SERVICE 3</div></div>
<div class="tile" style="left:721px;background:linear-gradient(160deg,#f2e23a,#f0c21c 60%,#e9731d)" role="img" aria-label="Construction tools and hard hat on yellow surface"><div class="label">SERVICE 4</div></div>
<div class="tile" style="left:956px;background:linear-gradient(180deg,#9c9d9e,#6f7072 60%,#4c4d4f)" role="img" aria-label="Concrete interior with steel staircase"><div class="label">SERVICE 5</div></div>
<div class="btn-raised" style="top:1611px">VIEW ALL SERVICES</div>

<section class="abs stats">
  <div class="stat blue"><strong>$2B+</strong><small>Worth of value created</small></div>
  <div class="stat dark"><strong>100+</strong><small>Clients</small></div>
  <div class="stat blue">
    <div class="stars">
      <svg width="36" height="36" viewBox="0 0 24 24"><path fill="#fff" d="M12 2l3 7h7l-5.6 4.3 2.1 7.2L12 16.3 5.5 20.5l2.1-7.2L2 9h7z"/></svg>
      <svg width="36" height="36" viewBox="0 0 24 24"><path fill="#fff" d="M12 2l3 7h7l-5.6 4.3 2.1 7.2L12 16.3 5.5 20.5l2.1-7.2L2 9h7z"/></svg>
      <svg width="36" height="36" viewBox="0 0 24 24"><path fill="#fff" d="M12 2l3 7h7l-5.6 4.3 2.1 7.2L12 16.3 5.5 20.5l2.1-7.2L2 9h7z"/></svg>
      <svg width="36" height="36" viewBox="0 0 24 24"><path fill="#fff" d="M12 2l3 7h7l-5.6 4.3 2.1 7.2L12 16.3 5.5 20.5l2.1-7.2L2 9h7z"/></svg>
      <svg width="36" height="36" viewBox="0 0 24 24"><path fill="#fff" d="M12 2l3 7h7l-5.6 4.3 2.1 7.2L12 16.3 5.5 20.5l2.1-7.2L2 9h7z"/></svg>
    </div>
    <small style="margin-top:14px">Accredited 'USA Excellent'<br>Green Star facilities</small>
  </div>
  <div class="stat dark"><strong>15+</strong><small>Years of experience</small></div>
</section>

<h2 class="section-title" style="top:2158px">OUR <span>PROJECT</span></h2>
<div class="photo" style="left:17px;top:2250px;width:381px;height:282px;background:linear-gradient(180deg,#cfd6dc,#9aa3ab 60%,#e3e6e9)" role="img" aria-label="Warehouse with racking"></div>
<div class="photo" style="left:17px;top:2540px;width:381px;height:282px;background:linear-gradient(180deg,#a33a3e,#e8eaec 35%,#f5f6f7)" role="img" aria-label="Bright empty white hall"></div>
<div class="photo" style="left:410px;top:2250px;width:382px;height:572px;background:linear-gradient(180deg,#f1f1f1,#d7d7d6 55%,#a9a8a5)" role="img" aria-label="Interior fit-out with scaffolding"></div>
<div class="photo" style="left:802px;top:2250px;width:381px;height:282px;background:linear-gradient(180deg,#3c3f43,#c9ccce 50%,#6a5a4d)" role="img" aria-label="Open plan office in industrial building"></div>
<div class="photo" style="left:802px;top:2540px;width:381px;height:282px;background:linear-gradient(180deg,#4d86cf,#b7cbe0 45%,#9b3a3e 75%,#8a8b8c)" role="img" aria-label="Logistics building with loading docks"></div>
<div class="btn-raised" style="top:2865px">VIEW ALL PROJECT</div>

<section class="abs clients">
  <h2 class="section-title" style="top:75px">OUR <span>CLIENTS</span></h2>
  <div class="client" style="left:54px"><i></i><span>Halden Ridge</span></div>
  <div class="client" style="left:195px"><i></i><span>Halden Ridge</span></div>
  <div class="client" style="left:336px"><i></i><span>Halden Ridge</span></div>
  <div class="client" style="left:478px"><i></i><span>Halden Ridge</span></div>
  <div class="client" style="left:619px"><i></i><span>Halden Ridge</span></div>
  <div class="client" style="left:760px"><i></i><span>Halden Ridge</span></div>
  <div class="client" style="left:902px"><i></i><span>Halden Ridge</span></div>
  <div class="client" style="left:1043px"><i></i><span>Halden Ridge</span></div>
</section>

<h2 class="section-title" style="top:3450px">WHAT <span>PEOPLE SAY</span> ABOUT US</h2>
<div class="abs avatar" role="img" aria-label="Client portrait"></div>
<svg class="arrow" style="left:64px" viewBox="0 0 54 54"><circle cx="27" cy="27" r="24" fill="none" stroke="#0a5ea8" stroke-width="3"/><path d="M31 17l-10 10 10 10" fill="none" stroke="#0a5ea8" stroke-width="3"/></svg>
<svg class="arrow" style="left:1078px" viewBox="0 0 54 54"><circle cx="27" cy="27" r="24" fill="none" stroke="#0a5ea8" stroke-width="3"/><path d="M23 17l10 10-10 10" fill="none" stroke="#0a5ea8" stroke-width="3"/></svg>
<p class="abs quote">Lorem ipsum dolor sit amet Lorem ipsum dolor sit Lorem ipsum dolor sitLorem ipsum dolor sitLorem ipsum dolor sitLorem.....</p>
<div class="abs who"><b>Marcus</b><small>Lorem Ipsum Dolor</small></div>

<section class="abs news">
  <h2 class="section-title" style="top:70px"><span>INDUSTRY</span> NEWS</h2>
</section>
<div class="card" style="left:17px"><div class="img" style="background:linear-gradient(160deg,#6d5a3c,#e7e2d6 50%,#f0c31d)" role="img" aria-label="Tools on construction plans"></div><p>Lorem ipsum dolor sit amet, consectetur adipiscing elit, sed do eiusmod tempor incididunt ut labore et dolore magna aliqua.</p><div class="more">Learn more</div></div>
<div class="card" style="left:428px"><div class="img" style="background:linear-gradient(160deg,#3a3a3a,#e9e9e9 45%,#d98a52)" role="img" aria-label="Desk with laptop and floor plans"></div><p>Lorem ipsum dolor sit amet, consectetur adipiscing elit, sed do eiusmod tempor incididunt ut labore et dolore magna aliqua.</p><div class="more">Learn more</div></div>
<div class="card" style="left:840px"><div class="img" style="background:linear-gradient(160deg,#f1f1f1,#c9c9c9 40%,#f3c51c)" role="img" aria-label="Hard hat and level on blueprints"></div><p>Lorem ipsum dolor sit amet, consectetur adipiscing elit, sed do eiusmod tempor incididunt ut labore et dolore magna aliqua.</p><div class="more">Learn more</div></div>
<div class="btn-raised" style="top:4557px">VIEW ALL NEWS</div>

<footer class="abs footer">
  <div class="foot-nav">HOME<br>ABOUT US<br>SERVICES<br>PROJECTS<br>NEWS<br>CONTACT</div>
  <div class="foot-form">For any inquiries, questions or commendations,<br>please call: +1 (555) 0142-0177 or fill out the following form</div>
  <div class="field" style="left:328px;top:84px;width:194px">Name</div>
  <div class="field" style="left:537px;top:84px;width:194px">Email</div>
  <div class="field" style="left:328px;top:126px;width:194px">Tel</div>
  <div class="field" style="left:537px;top:126px;width:194px">Subject</div>
  <div class="field" style="left:328px;top:168px;width:403px;height:60px">Message</div>
  <div class="send">Send</div>
  <div class="follow">FOLLOW US</div>
  <div class="follow-icons" aria-label="social links"><span></span><span></span><span></span></div>
  <div class="legal">© Halden Ridge Construction 2022 | license No xxx<br>Company Policies and Documents</div>
</footer>

</body>
</html>
```